Property developer, money partner needs business card design using logo concept provided

Our company develops residential properties, does money lends for joint ventures in property deals and finds property deals for other money partners. We have provided a basic logo for you to work from. Any graphic or logo design on the card is to communicate development and finance collaboration. Color choice is not so important for us, but color choice does need to reflect professionalism.

```html
<!DOCTYPE html>
<html lang="en">
<head>
<meta charset="utf-8">
<title>Brightlot Property Solutions – Business Card</title>
<link href="https://fonts.googleapis.com/css2?family=Poppins:wght@400;500;600&family=PT+Sans:wght@400&display=swap" rel="stylesheet">
<style>
  :root {
    --backdrop: #2e2e2e;
    --card-white: #ffffff;
    --brand-blue: #0868b0;
    --brand-navy: #174a9a;
    --ink: #1f1f1f;
    --logo-ink: #1a1a1a;
  }
  html, body {
    margin: 0;
    padding: 0;
    width: 1200px;
    height: 1000px;
    overflow: hidden;
    background: var(--backdrop);
  }
  .canvas {
    position: relative;
    width: 1200px;
    height: 1000px;
  }
  .card {
    position: absolute;
    left: 254px;
    width: 692px;
    height: 396px;
    overflow: hidden;
  }
  .card--front { top: 67px; background: var(--card-white); }
  .card--back { top: 537px; background: var(--brand-blue); }

  /* Front */
  .name-tab {
    position: absolute;
    left: 0; top: 121px;
    width: 25px; height: 40px;
    background: var(--brand-blue);
  }
  .holder-name {
    position: absolute;
    left: 39px; top: 119px;
    margin: 0;
    font-family: "Poppins", sans-serif;
    font-weight: 600;
    font-size: 23px;
    letter-spacing: 0.5px;
    color: var(--brand-navy);
  }
  .holder-tagline {
    position: absolute;
    left: 40px; top: 145px;
    margin: 0;
    font-family: "Poppins", sans-serif;
    font-weight: 400;
    font-size: 14px;
    color: var(--ink);
  }
  .contact-list {
    position: absolute;
    left: 38px; top: 232px;
    margin: 0; padding: 0;
    list-style: none;
    font-family: "PT Sans", sans-serif;
    font-size: 16px;
    line-height: 20px;
    color: var(--ink);
  }
  .contact-item {
    display: flex;
    align-items: flex-start;
    margin-bottom: 3px;
  }
  .contact-icon {
    width: 14px; height: 14px;
    margin: 3px 9px 0 0;
    flex: none;
    fill: var(--brand-navy);
  }
  .front-stripe {
    position: absolute;
    left: 0; bottom: 0;
    width: 100%; height: 9px;
    background: var(--brand-blue);
  }
  .brand-block {
    position: absolute;
    text-align: center;
    font-family: "Poppins", sans-serif;
    font-weight: 500;
    margin: 0;
  }
  .brand-block--front { left: 390px; top: 58px; width: 272px; color: var(--logo-ink); }
  .brand-block--back { left: 221px; top: 50px; width: 250px; color: var(--card-white); }
  .brand-disc {
    display: block;
    margin: 0 auto;
    border-radius: 50%;
  }
  .brand-block--front .brand-disc { width: 176px; height: 176px; background: var(--brand-blue); margin-bottom: 36px; }
  .brand-block--back .brand-disc { width: 196px; height: 196px; background: var(--card-white); margin-bottom: 48px; }
  .brand-name {
    display: block;
    letter-spacing: 7px;
    line-height: 1.1;
  }
  .brand-block--front .brand-name { font-size: 25px; }
  .brand-block--back .brand-name { font-size: 21px; }
  .brand-descriptor {
    display: block;
    letter-spacing: 3px;
    line-height: 1.2;
  }
  .brand-block--front .brand-descriptor { font-size: 18px; }
  .brand-block--back .brand-descriptor { font-size: 15px; }
  .brand-acn {
    display: block;
    letter-spacing: 3px;
    margin-top: 2px;
  }
  .brand-block--front .brand-acn { font-size: 11px; }
  .brand-block--back .brand-acn { font-size: 10px; }
</style>
</head>
<body>
<main class="canvas">

  <section class="card card--front" aria-label="Business card front">
    <div class="name-tab"></div>
    <h1 class="holder-name">DANIEL MERCER</h1>
    <p class="holder-tagline">Tagline Here</p>

    <ul class="contact-list">
      <li class="contact-item">
        <svg class="contact-icon" viewBox="0 0 14 14" aria-hidden="true"><path d="M7 0a5 5 0 0 0-5 5c0 3.6 5 9 5 9s5-5.4 5-9a5 5 0 0 0-5-5zm0 7a2 2 0 1 1 0-4 2 2 0 0 1 0 4z"/></svg>
        <span>482 Harbor Avenue,<br>Springfield, IL 6270</span>
      </li>
      <li class="contact-item">
        <svg class="contact-icon" viewBox="0 0 14 14" aria-hidden="true"><path d="M3.5 0h7a1 1 0 0 1 1 1v12a1 1 0 0 1-1 1h-7a1 1 0 0 1-1-1V1a1 1 0 0 1 1-1zm.5 1.5v9.5h6V1.5zM7 11.6a.8.8 0 1 0 0 1.6.8.8 0 0 0 0-1.6z"/></svg>
        <span>(555) 214-0000</span>
      </li>
      <li class="contact-item">
        <svg class="contact-icon" viewBox="0 0 14 14" aria-hidden="true"><path d="M3 1l2 3-1.3 1.3a8 8 0 0 0 4.9 4.9L10 9l3 2-1.2 2C6 13 1 8 1 2.2z"/></svg>
        <span>(555) 000-0189</span>
      </li>
      <li class="contact-item">
        <svg class="contact-icon" viewBox="0 0 14 14" aria-hidden="true"><path d="M0 3h14v1L7 8 0 4zm0 2.6l7 4 7-4V12H0z"/></svg>
        <span>info@brightlotproperty.com</span>
      </li>
      <li class="contact-item">
        <svg class="contact-icon" viewBox="0 0 14 14" aria-hidden="true"><path d="M7 0a7 7 0 1 0 0 14A7 7 0 0 0 7 0zm0 1.5c.6 0 1.5 1.6 1.7 4H5.3C5.5 3.1 6.4 1.5 7 1.5zM5.3 7h3.4c-.2 2.4-1.1 4-1.7 4S5.5 9.4 5.3 7zM1.6 7h2.2c.1 1.6.5 2.9 1 3.8A5.5 5.5 0 0 1 1.6 7zm8.6 0h2.2a5.5 5.5 0 0 1-3.2 3.8c.5-.9.9-2.2 1-3.8zM1.6 5.5a5.5 5.5 0 0 1 3.2-3.8c-.5.9-.9 2.2-1 3.8zm8.6 0c-.1-1.6-.5-2.9-1-3.8a5.5 5.5 0 0 1 3.2 3.8z"/></svg>
        <span>www.brightlotproperty.com</span>
      </li>
    </ul>

    <p class="brand-block brand-block--front">
      <span class="brand-disc"></span>
      <span class="brand-name">BRIGHTLOT</span>
      <span class="brand-descriptor">Property Solutions</span>
      <span class="brand-acn">A.C.N 000 123 456</span>
    </p>

    <div class="front-stripe"></div>
  </section>

  <section class="card card--back" aria-label="Business card back">
    <p class="brand-block brand-block--back">
      <span class="brand-disc"></span>
      <span class="brand-name">BRIGHTLOT</span>
      <span class="brand-descriptor">Property Solutions</span>
      <span class="brand-acn">A.C.N 000 123 456</span>
    </p>
  </section>

</main>
</body>
</html>
```